Marlowe Candles scented candles made from soy wax

I want to make my Squarespace website look more professional. I need a website with an online store and workshops for my business with scented candles made from soy wax, wax melts, room fragrances, car fragrances, fragrance lamps and accessories. The design of the website should match my candle labels. The flower and the Marlowe Candles font must be in the logo. My current website: www.marlowecandles.ch

```html
<!DOCTYPE html>
<html lang="de">
<head>
<meta charset="utf-8">
<title>Marlowe Candles – Duftkerzen aus Sojawachs</title>
<link href="https://fonts.googleapis.com/css2?family=Oswald:wght@400;500;600&family=Libre+Franklin:wght@300;400;500;600&display=swap" rel="stylesheet">
<style>
  :root{
    --gold:#edd68a;
    --gold-pale:#faf1d8;
    --ink:#222222;
    --charcoal:#333333;
    --grey-band:#f3f3f3;
    --white:#ffffff;
  }
  *{margin:0;padding:0;box-sizing:border-box;}
  html,body{width:1200px;height:3130px;overflow:hidden;background:var(--white);}
  body{position:relative;font-family:"Libre Franklin",Arial,sans-serif;color:var(--ink);}
  .heading{font-family:"Oswald",Arial,sans-serif;font-weight:500;color:var(--charcoal);}
  .btn{position:absolute;display:flex;align-items:center;justify-content:center;background:var(--charcoal);color:var(--white);font-family:"Oswald",Arial,sans-serif;font-size:16px;letter-spacing:-.2px;}
  .social-dot{display:block;width:22px;height:22px;border-radius:50%;background:var(--ink);}

  /* header */
  .site-header{position:absolute;left:0;top:0;width:1200px;height:96px;background:var(--white);}
  .main-nav{position:absolute;left:113px;top:38px;display:flex;gap:23px;font-size:13.5px;}
  .brand{position:absolute;left:480px;top:30px;width:240px;text-align:center;font-family:"Oswald",Arial,sans-serif;font-weight:500;font-size:22px;color:var(--ink);}
  .header-social{position:absolute;right:112px;top:32px;display:flex;gap:18px;align-items:center;}

  /* hero */
  .hero{position:absolute;left:0;top:96px;width:1200px;height:600px;}
  .hero-photo{position:absolute;inset:0;background:
      radial-gradient(ellipse 230px 300px at 830px 330px,#3a3430 0%,#2a2624 60%,rgba(42,38,36,0) 100%),
      linear-gradient(180deg,#a07c50 0%,#8d7152 45%,#9fa1aa 60%,#b3b5bd 100%);}
  .hero-welcome{position:absolute;left:111px;top:154px;font-family:"Oswald",Arial,sans-serif;font-size:40px;color:var(--white);font-weight:400;}
  .hero-title{position:absolute;left:108px;top:222px;font-family:"Oswald",Arial,sans-serif;font-weight:600;font-size:80px;line-height:89px;color:var(--gold);}
  .hero-cta{position:absolute;left:112px;top:434px;width:122px;height:53px;border:2px solid var(--gold);color:var(--white);display:flex;align-items:center;justify-content:center;font-family:"Oswald",Arial,sans-serif;font-size:16px;}

  /* intro */
  .intro{position:absolute;left:0;top:696px;width:1200px;height:253px;background:var(--gold);}
  .intro-brand{position:absolute;left:109px;top:111px;font-family:"Libre Franklin",Arial,sans-serif;font-weight:600;font-size:26px;color:var(--ink);}
  .intro-text{position:absolute;left:351px;top:47px;width:737px;font-size:14.6px;font-weight:400;line-height:25.6px;text-align:justify;color:#333;}

  /* best sellers */
  .bestsellers{position:absolute;left:0;top:949px;width:1200px;height:519px;}
  .bestsellers h2{position:absolute;left:115px;top:170px;font-size:48px;}
  .carousel-arrows{position:absolute;left:1048px;top:72px;}
  .product-card{position:absolute;top:105px;width:185px;}
  .product-card .photo{width:185px;height:276px;}
  .product-card .name{margin-top:13px;font-size:15px;font-weight:500;color:#333;}
  .product-card .price{margin-top:8px;font-size:12px;font-weight:600;color:#333;}

  /* workshops */
  .workshops{position:absolute;left:0;top:1468px;width:1200px;height:600px;background:var(--grey-band);}
  .workshop-frame{position:absolute;left:112px;top:72px;width:488px;height:456px;border:7px solid var(--gold);}
  .workshop-frame .photo{width:100%;height:100%;background:linear-gradient(160deg,#c7a27a 0%,#b38e67 40%,#3b3936 70%,#62605c 100%);}
  .workshops h2{position:absolute;left:663px;top:156px;font-size:50px;white-space:nowrap;}
  .workshops p{position:absolute;left:663px;top:251px;width:418px;font-size:15px;line-height:25.6px;text-align:justify;color:#444;}

  /* must haves */
  .must-haves{position:absolute;left:0;top:2068px;width:1200px;height:710px;}
  .must-haves h2{position:absolute;left:0;width:1200px;top:74px;text-align:center;font-size:48px;}
  .feature{position:absolute;top:168px;width:305px;text-align:center;}
  .feature .photo{width:305px;height:327px;}
  .feature h3{margin-top:22px;font-family:"Oswald",Arial,sans-serif;font-weight:500;font-size:28px;color:var(--charcoal);}
  .feature .btn{left:74px;top:408px;width:158px;height:54px;}

  /* footer */
  .site-footer{position:absolute;left:0;top:2778px;width:1200px;height:352px;background:var(--gold-pale);}
  .quick-title{position:absolute;left:111px;top:70px;font-size:16px;font-weight:500;}
  .quick-links{position:absolute;left:115px;top:104px;list-style:none;font-size:17.5px;line-height:25.8px;color:#333;}
  .footer-social{position:absolute;left:111px;top:291px;display:flex;gap:14px;}
  .signup-label{position:absolute;left:755px;top:70px;font-size:16px;color:#333;}
  .signup-input{position:absolute;left:755px;top:112px;width:333px;height:63px;border:1px solid #cfcfcf;background:var(--white);font-size:16px;padding-left:22px;display:flex;align-items:center;color:#333;}
  .signup-btn{left:755px;top:202px;width:158px;height:53px;}
  .copyright{position:absolute;left:0;width:1200px;top:299px;text-align:center;font-size:15.5px;color:#333;}
</style>
</head>
<body>

<header class="site-header">
  <nav class="main-nav">
    <span>Shop</span><span>Pos</span><span>Sojawachs</span><span>Über Mc</span><span>Workshop</span><span>Agb</span>
  </nav>
  <div class="brand">Marlowe Candles</div>
  <div class="header-social">
    <span class="social-dot" aria-label="Soziales Netzwerk"></span>
    <span class="social-dot" aria-label="Soziales Netzwerk"></span>
    <svg width="30" height="28" viewBox="0 0 30 28" fill="none" stroke="#222" stroke-width="1.8" aria-label="Warenkorb">
      <path d="M1 3h5l4 15h14l4-11H8"/>
      <circle cx="12" cy="24" r="2"/><circle cx="22" cy="24" r="2"/>
    </svg>
  </div>
</header>

<section class="hero">
  <div class="hero-photo" role="img" aria-label="Schwarzes Windlicht mit goldenem Baummotiv und brennender Kerze vor Holzwand"></div>
  <div class="hero-welcome">Willkommen zu</div>
  <h1 class="hero-title">Duftkerzen aus<br>Sojawachs</h1>
  <div class="hero-cta">Jetzt einkaufen</div>
</section>

<section class="intro">
  <div class="intro-brand">Marlowe Candles</div>
  <p class="intro-text">Marlowe Candles aus Sojawachs sind handgemacht und mit viel Liebe gegossen, im schönen Rheintal in der Schweiz. Sojawachs ist pflanzlich und seine Brennzeit ist ca 30-40% länger als herkömmliche Kerzen aus Paraffin oder Stearin. Sojakerzen brennen sauberer und Sojawachs belastet die Atemluft nicht. Die ausgewählten Düfte für meine Kerzen sind sanft, von exzellenter Qualität, sorgfältig geprüft und eine Wohltat für jeden Kerzenliebhaber. Jede Kerze ist von Hand dekoriert mit Wachsblumen und Trockenblumen. Das Design passt zu jeder Inneneinrichtung und die Kerzen sind ein Blickfang, wo immer sie stehen.</p>
</section>

<section class="bestsellers">
  <h2 class="heading">Best Sellers</h2>
  <div class="btn" style="left:112px;top:251px;width:156px;height:53px;">Kaufen Sie Bestseller</div>
  <svg class="carousel-arrows" width="40" height="26" viewBox="0 0 40 26" fill="none" stroke-width="2">
    <path d="M14 3 6 13l8 10" stroke="#222"/>
    <path d="M28 3l8 10-8 10" stroke="#aaa"/>
  </svg>
  <div class="product-card" style="left:510px;">
    <div class="photo" role="img" aria-label="Schwarze Duftkerze mit Blumen auf kariertem Tischtuch" style="background:linear-gradient(180deg,#8c7a62 0%,#6d6259 45%,#2b2a2a 70%,#8a8689 100%);"></div>
    <div class="name">Alle Artikel</div><div class="price">ab CHF 15.00</div>
  </div>
  <div class="product-card" style="left:708px;">
    <div class="photo" role="img" aria-label="Duftkerze im Glas mit Trockenblumen im Garten" style="background:linear-gradient(180deg,#6f6a4e 0%,#8b7c58 35%,#d2c4a0 60%,#9b9494 100%);"></div>
    <div class="name">Duftkerzen</div><div class="price">ab CHF 15.00</div>
  </div>
  <div class="product-card" style="left:905px;">
    <div class="photo" role="img" aria-label="Raumduft mit Stäbchen und schwarzer Röhre am Fenster" style="background:linear-gradient(90deg,#8e8f93 0%,#2a2a2c 30%,#b7a07f 60%,#c9ad86 100%);"></div>
    <div class="name">Raumdüfte</div><div class="price">ab CHF 15.00</div>
  </div>
</section>

<section class="workshops">
  <div class="workshop-frame">
    <div class="photo" role="img" aria-label="Verschiedene Duftkerzen in Gläsern vor Holzwand"></div>
  </div>
  <h2 class="heading">Workshops For Businesss</h2>
  <p>Lorem ipsum dolor sit amet, consectetur adipiscing elit, sed do eiusmod tempor incididunt ut labore et dolore magna aliqua.</p>
  <div class="btn" style="left:663px;top:377px;width:158px;height:53px;">Kaufen Sie Bestseller</div>
</section>

<section class="must-haves">
  <h2 class="heading">Must Haves</h2>
  <div class="feature" style="left:113px;">
    <div class="photo" role="img" aria-label="Windlicht schwarz mit goldenem Baummotiv" style="background:radial-gradient(ellipse at 50% 25%,#d9b27a 0%,#5a4a3a 35%,#1f1c1b 70%);"></div>
    <h3>Windlicht Schwarz Gold</h3>
    <div class="btn">Jetzt kaufen</div>
  </div>
  <div class="feature" style="left:448px;">
    <div class="photo" role="img" aria-label="Duftkerze Magnolie Musk im Glas" style="background:linear-gradient(180deg,#e8e6e4 0%,#cfc9c4 30%,#2b2a28 45%,#2b2a28 75%,#e5e2dd 100%);"></div>
    <h3>Duftkerze Magnolie Musk</h3>
    <div class="btn">Jetzt kaufen</div>
  </div>
  <div class="feature" style="left:783px;">
    <div class="photo" role="img" aria-label="Raumduft mit Stäbchen und schwarzer Verpackungsröhre" style="background:linear-gradient(90deg,#b49474 0%,#222 25%,#2a2a2a 40%,#c9ac88 60%,#d6bb95 100%);"></div>
    <h3>Raumduft</h3>
    <div class="btn">Jetzt kaufen</div>
  </div>
</section>

<footer class="site-footer">
  <div class="quick-title">Quick Links</div>
  <ul class="quick-links">
    <li>Shop</li><li>Pos</li><li>Sojawachs</li><li>Über Mc</li><li>Workshop</li><li>Agb</li>
  </ul>
  <div class="footer-social">
    <span class="social-dot" aria-label="Soziales Netzwerk"></span>
    <span class="social-dot" aria-label="Soziales Netzwerk"></span>
  </div>
  <div class="signup-label">Sign up to receive news and updates.</div>
  <div class="signup-input">Enter Email</div>
  <div class="btn signup-btn">schicken</div>
  <div class="copyright">©Copyrights 2024 Marlowecandles &nbsp;| &nbsp; All Rights Reserved</div>
</footer>

</body>
</html>
```